Varga Lillas Physiotherapy Business Card Vienna

We need a business card design for a newly created Physiotherapy company based in Vienna Austria.
We seek a simple, modern, minimalist design without too much color variation. The font should look young/fresh, but definitely not childish or so. Since we are a starting Business, we currently haven't got a logo, if you feel like a logo would fit your design, feel free to use one, but it's not necessary.
Target Market(s)
Healthcare, young and elderly people with mobility issues
Industry/Entity Type
Health And Wellness
Contact Information for Business Card
Name: Lilla Varga
Title description: Physiotherapist
Phone num: +43 664 5290 4816
e-mail: lilla.praxis@brelomail.com
Colors
Designer to choose colors to be used in the design.
Requirements
Must have
- Final design language must be in German, basically, the Title Description needs to be "Physiotherapeutin" the other details remain as in the English Language.
Nice to have
- Simple, modern, minimalist design
Should not have
- too many colors, Obvious use of a skeleton, skull, spline

```html
<!DOCTYPE html>
<html lang="de">
<head>
<meta charset="utf-8">
<title>Lilla Varga – Physiotherapeutin</title>
<link rel="stylesheet" href="https://fonts.googleapis.com/css2?family=Montserrat:wght@700&family=Nunito:wght@400;600&display=swap">
<style>
  :root {
    --backdrop: #e8d035;
    --card: #1a1c2c;
    --ink: #ffffff;
    --graphic-light: #f4f4f6;
    --graphic-shade: #c9cad2;
  }
  * { margin: 0; padding: 0; box-sizing: border-box; }
  html, body {
    width: 1200px;
    height: 1200px;
    overflow: hidden;
    background: var(--backdrop);
  }
  .business-card {
    position: absolute;
    left: 100px;
    top: 300px;
    width: 1000px;
    height: 600px;
    background: var(--card);
    color: var(--ink);
  }
  .card-frame {
    position: absolute;
    left: 86px;
    top: 131px;
    width: 837px;
    height: 338px;
    border: 3px solid var(--ink);
  }
  .identity {
    position: absolute;
    right: 102px;
    top: 145px;
    text-align: right;
  }
  .identity-name {
    font-family: "Montserrat", sans-serif;
    font-weight: 700;
    font-size: 52px;
    line-height: 1;
    letter-spacing: 1px;
  }
  .identity-title {
    margin-top: 16px;
    font-family: "Nunito", sans-serif;
    font-weight: 400;
    font-size: 17px;
    letter-spacing: 9.4px;
    margin-right: -9px;
  }
  .fitness-graphic {
    position: absolute;
    left: 148px;
    top: 268px;
    width: 704px;
    height: 60px;
    background: linear-gradient(90deg, var(--graphic-light), var(--graphic-shade), var(--graphic-light));
  }
  .contact-list {
    position: absolute;
    left: 112px;
    top: 348px;
    list-style: none;
    font-family: "Nunito", sans-serif;
    font-size: 21px;
  }
  .contact-item {
    display: flex;
    align-items: center;
    gap: 14px;
    height: 50px;
  }
  .contact-icon { width: 26px; height: 26px; flex: none; }
</style>
</head>
<body>
  <main class="business-card">
    <div class="card-frame"></div>

    <header class="identity">
      <h1 class="identity-name">LILLA VARGA</h1>
      <p class="identity-title">PHYSIOTHERAPEUTIN</p>
    </header>

    <div class="fitness-graphic" role="img" aria-label="Horizontal barbell graphic spanning the card"></div>

    <ul class="contact-list">
      <li class="contact-item">
        <svg class="contact-icon" viewBox="0 0 24 24" aria-hidden="true">
          <path fill="#ffffff" d="M6.6 10.8a15.1 15.1 0 0 0 6.6 6.6l2.2-2.2c.3-.3.7-.4 1-.2 1.1.4 2.3.6 3.6.6.6 0 1 .4 1 1V20c0 .6-.4 1-1 1A17 17 0 0 1 3 4c0-.6.4-1 1-1h3.5c.6 0 1 .4 1 1 0 1.3.2 2.5.6 3.6.1.3 0 .7-.2 1z"/>
        </svg>
        <span class="contact-text">(+43) 664 5290 4816</span>
      </li>
      <li class="contact-item">
        <svg class="contact-icon" viewBox="0 0 24 24" aria-hidden="true">
          <rect x="2" y="5" width="20" height="14" fill="#ffffff"/>
          <path d="M2 5l10 8 10-8" fill="none" stroke="#1a1c2c" stroke-width="2"/>
        </svg>
        <span class="contact-text">lilla.praxis@brelomail.com</span>
      </li>
    </ul>
  </main>
</body>
</html>
```